First Reponders Promotion poster/flyer

Our Yoga studio is introducing an ongoing promotion for all First Responders, Police/Nurse/Paramedic/Firefighters/Doctors
$22pw for Unlimited access to our Inner city Studio which will become a sanctuary for the people who look after us. Tag line: You look after us, let us look after you. The benefits of yoga, reduce stress, clear mind, healthy body. Feel free to use other assets, and be as creative as you like I have just put images and designs as a guide.

Target Market(s)

Emergency Services Tasmania

Industry/Entity Type

Emergency Services

Requirements
Must have
• Solvaro Logo/Address 41 Kelmora St/ website www.solvarostudio.com.a/ sign up online and just bring in current work Id at checkin/$22pw Unlimited classes/Australian market so can't look like usa or any other countries
Nice to have
• words , inner city Sanctuary
Should not have
• Foreign Country images

```html
<!DOCTYPE html>
<html lang="en">
<head>
<meta charset="utf-8">
<title>Solvaro – First Responders Offer</title>
<link href="https://fonts.googleapis.com/css2?family=Poppins:wght@300;400;500;600;700;800;900&family=Oswald:wght@400;500&display=swap" rel="stylesheet">
<style>
:root{
  --orange:#eca92f;
  --orange-deep:#e89b22;
  --sand:#f1d66a;
  --black:#111111;
  --charcoal:#333333;
  --white:#ffffff;
  --stage:#cfcfcf;
  --line:#f0b440;
}
*{box-sizing:border-box;margin:0;padding:0}
html,body{width:685px;height:1200px;overflow:hidden}
body{background:var(--stage);font-family:'Poppins',sans-serif;color:var(--black);position:relative}
.flyer{position:absolute;left:0;top:116px;width:685px;height:967px;background:var(--white);box-shadow:0 4px 14px rgba(0,0,0,.25);overflow:hidden}
.abs{position:absolute}

.brand{left:50px;top:38px;width:260px;text-align:center}
.brand-name{font-size:30px;font-weight:500;letter-spacing:17px;line-height:1;padding-left:17px}
.brand-tag{margin-top:22px;font-size:11px;font-weight:500;letter-spacing:5px}

.hero{left:0;top:136px;width:685px;height:238px;background:var(--orange)}
.hero-art{position:absolute;left:300px;top:0;width:385px;height:238px;background:linear-gradient(100deg,var(--orange) 0%,var(--sand) 45%,#efc65a 100%)}
.kicker{left:50px;top:40px;font-size:23px;font-weight:700;color:var(--white);letter-spacing:.3px;line-height:1}
.rule{height:3px;background:var(--white);width:259px;left:50px}
.headline{left:48px;top:82px;line-height:.95}
.headline .light{display:block;font-size:42px;font-weight:300;letter-spacing:-.5px}
.headline .bold{display:block;font-size:46px;font-weight:800;letter-spacing:-1px}

.offer{left:51px;top:374px;width:591px;height:112px;background:var(--black);border-radius:0 0 8px 8px;overflow:hidden}
.offer-price{position:absolute;right:0;top:0;width:179px;height:112px;background:var(--charcoal)}
.offer-title{left:24px;top:24px;font-size:22px;font-weight:700;line-height:1.05;color:var(--white)}
.offer-title span{color:var(--orange)}
.offer-copy{left:167px;top:14px;font-size:17px;color:var(--white);line-height:1.22}
.offer-sep{left:412px;top:20px;width:1px;height:68px;background:#888}
.price-for{left:28px;top:18px;font-size:22px;color:var(--white);font-weight:400;line-height:1}
.price-amt{left:28px;top:44px;font-size:34px;font-weight:800;color:var(--orange);line-height:1}
.price-amt sup{font-size:18px;vertical-align:14px}

.helps{left:51px;top:525px;width:308px;height:85px;border:1.5px solid var(--line);border-radius:4px}
.helps-label{left:0;top:-12px;background:var(--white);padding-right:8px;font-size:16px;font-weight:700;color:var(--orange)}
.help{position:absolute;top:22px;text-align:center;font-size:13px;font-weight:600}
.help .dot{display:block;margin:0 auto 2px;width:30px;height:30px;border-radius:50%;background:var(--black);position:relative}
.help .dot::after{content:"";position:absolute;left:10px;top:9px;width:10px;height:12px;border-radius:4px;background:var(--orange)}
.help-sep{position:absolute;top:18px;width:1px;height:50px;background:#ddd}

.date{left:374px;top:527px;width:267px;height:82px;background:var(--orange);border-radius:4px}
.date-box{position:absolute;left:0;top:0;width:137px;height:82px;background:var(--black);border-radius:4px;border:3px solid var(--orange)}
.date-day{position:absolute;left:0;width:131px;top:4px;text-align:center;background:var(--orange);font-size:33px;font-weight:800;line-height:38px;border-radius:4px 4px 0 0}
.date-year{position:absolute;left:0;width:131px;top:44px;text-align:center;font-size:26px;color:var(--white);letter-spacing:7px;line-height:30px}
.date-addr{position:absolute;left:155px;top:36px;font-size:15px;font-weight:500;line-height:1.2}
.date-pin{position:absolute;left:156px;top:6px}

.roles{left:52px;top:670px;width:580px;height:80px;display:flex;justify-content:space-between}
.role{width:75px;height:75px;border-radius:50%;border:1.5px solid transparent;border-bottom-color:var(--line);border-left-color:var(--line);border-right-color:var(--line);display:flex;flex-direction:column;align-items:center;justify-content:center;font-family:'Oswald',sans-serif;font-size:11px;text-transform:uppercase}
.role svg{margin-top:-34px;margin-bottom:14px}

.signup{left:54px;top:781px;font-size:13px;font-weight:600;line-height:1.2;border-left:3px solid var(--orange);padding-left:6px}
.crew{left:45px;top:822px;width:345px;height:145px;background:linear-gradient(90deg,#3f6fa8,#5c8a6e 50%,#e1a73a)}

.divider{left:414px;top:782px;width:1px;height:120px;background:#aaa}
.q-bulb{left:431px;top:788px}
.q-title{left:465px;top:785px;font-size:32px;font-weight:900;color:var(--orange);line-height:1;letter-spacing:-1px}
.q-sub{left:465px;top:818px;font-size:14px;font-weight:500}
.q-ask{left:440px;top:848px;font-size:15px;font-weight:700}
.q-ans{left:455px;top:868px;font-size:10px;line-height:1.2}
.q-warn{left:440px;top:870px;width:0;height:0;border-left:5px solid transparent;border-right:5px solid transparent;border-bottom:9px solid var(--orange)}

.site{left:358px;top:900px;width:287px;height:30px;background:var(--orange);border-radius:0 15px 15px 0;font-size:17px;font-weight:700;line-height:30px;text-align:right;padding-right:17px;letter-spacing:.5px}
</style>
</head>
<body>
<main class="flyer">
  <header class="abs brand">
    <div class="brand-name">SOLVARO</div>
    <div class="brand-tag">MIND+BODY+SPIRIT</div>
  </header>

  <section class="abs hero">
    <div class="hero-art" role="img" aria-label="Silhouettes of three people in yoga poses among bamboo, in warm yellow tones"></div>
    <p class="abs kicker">YOU LOOK AFTER US</p>
    <div class="abs rule" style="top:72px"></div>
    <h1 class="abs headline"><span class="light">LET US LOOK</span><span class="bold">AFTER YOU</span></h1>
    <div class="abs rule" style="top:174px"></div>
  </section>

  <section class="abs offer">
    <div class="offer-price">
      <p class="abs price-for">FOR</p>
      <p class="abs price-amt"><sup>$</sup>22PW</p>
    </div>
    <p class="abs offer-title">UNLIMITED<br><span>ACCESS</span></p>
    <p class="abs offer-copy">to our classes in our<br>beautiful inner-city Studio<br>Sanctuary</p>
    <div class="abs offer-sep"></div>
  </section>

  <section class="abs helps">
    <p class="abs helps-label">YOGA HELPS</p>
    <div class="help" style="left:20px"><span class="dot"></span>Stress</div>
    <div class="help-sep" style="left:85px"></div>
    <div class="help" style="left:102px"><span class="dot"></span>Mental Health</div>
    <div class="help-sep" style="left:215px"></div>
    <div class="help" style="left:233px"><span class="dot"></span>Fitness</div>
  </section>

  <section class="abs date">
    <div class="date-box">
      <div class="date-day">JULY 1</div>
      <div class="date-year">2022</div>
    </div>
    <svg class="date-pin" width="22" height="28" viewBox="0 0 22 28"><path d="M11 1C5.5 1 1.5 5 1.5 10.5 1.5 17 11 27 11 27s9.5-10 9.5-16.5C20.5 5 16.5 1 11 1z" fill="#e8453c" stroke="#fff" stroke-width="1.5"/><circle cx="11" cy="10.5" r="4" fill="#fff"/></svg>
    <p class="date-addr">41 Kelmora St,<br>Hobart</p>
  </section>

  <section class="abs roles">
    <div class="role"><svg width="30" height="30" viewBox="0 0 30 30"><path d="M11 2h8v9l8-4 4 7-8 4 8 4-4 7-8-4v9h-8v-9l-8 4-4-7 8-4-8-4 4-7 8 4z" fill="#111" transform="scale(.9) translate(1,1)"/></svg>Paramedic</div>
    <div class="role"><svg width="34" height="26" viewBox="0 0 34 26"><rect x="1" y="6" width="22" height="15" fill="#111"/><path d="M23 10h6l4 6v5H23z" fill="#111"/><circle cx="8" cy="22" r="3" fill="#111" stroke="#fff"/><circle cx="27" cy="22" r="3" fill="#111" stroke="#fff"/><path d="M10 10h3v3h3v3h-3v3h-3v-3H7v-3h3z" fill="#fff"/></svg>Ambulance</div>
    <div class="role"><svg width="26" height="30" viewBox="0 0 26 30"><path d="M5 8Q13 0 21 8v5H5z" fill="#111"/><circle cx="13" cy="17" r="7" fill="#fff" stroke="#111" stroke-width="3"/><path d="M3 13h4v16H3zM19 13h4v16h-4z" fill="#111"/></svg>Nurse</div>
    <div class="role"><svg width="32" height="26" viewBox="0 0 32 26"><path d="M2 10Q16 0 30 10l-3 6H5z" fill="#111"/><rect x="4" y="17" width="24" height="5" rx="2" fill="#111"/><circle cx="16" cy="9" r="2.5" fill="#fff"/></svg>Police</div>
    <div class="role"><svg width="30" height="30" viewBox="0 0 30 30"><path d="M6 8Q15 0 24 8l2 3H4z" fill="#111"/><circle cx="15" cy="15" r="5" fill="#111"/><path d="M4 30q0-9 11-9t11 9z" fill="#111"/></svg>Firefighters</div>
    <div class="role"><svg width="28" height="30" viewBox="0 0 28 30"><circle cx="14" cy="9" r="7" fill="#111"/><path d="M2 30q0-12 12-12t12 12z" fill="#111"/></svg>SES</div>
    <div class="role"><svg width="28" height="30" viewBox="0 0 28 30"><circle cx="14" cy="8" r="6" fill="#111"/><path d="M2 30q0-14 12-14t12 14z" fill="#111"/><circle cx="18" cy="24" r="2.5" fill="#fff"/></svg>Doctors</div>
  </section>

  <p class="abs signup">Just sign up on Website and bring in you Current<br>ID for verification</p>
  <div class="abs crew" role="img" aria-label="Illustrated group of first responders: police, doctors, nurses, firefighters and emergency workers"></div>

  <div class="abs divider"></div>
  <svg class="abs q-bulb" width="26" height="34" viewBox="0 0 26 34"><circle cx="13" cy="13" r="9" fill="#f4c64a" stroke="#111" stroke-width="1.5"/><rect x="9" y="22" width="8" height="7" fill="#111"/><path d="M1 6l3 2M25 6l-3 2M13 0v3" stroke="#111" stroke-width="1.5"/></svg>
  <p class="abs q-title">Questions</p>
  <p class="abs q-sub">they might have</p>
  <p class="abs q-ask">IS THERE ANY CONTRACT?</p>
  <div class="abs q-warn"></div>
  <p class="abs q-ans">No only email 2 weeks prior<br>to cancel</p>

  <p class="abs site">www.solvarostudio.com.a</p>
</main>
</body>
</html>
```